" A Vendaluz Store comercializa produtos nos seguintes segmentos: automotivo, cine e foto, componentes, cuidados pessoais, eletrodomésticos e eletroportáteis, eletrônicos, games, informatica, instrumentos musicais, materiais elétricos, som profissional e telefonia além de produtos de decoração. Tem como objetivo fornecer produtos de excelência e proporcionar uma marcante experiência de compra na modalidade e-commerce. "

```html
<!DOCTYPE html>
<html lang="pt-BR">
<head>
<meta charset="utf-8">
<title>Vendaluz Store – Assinatura de e-mail</title>
<link rel="stylesheet" href="https://fonts.googleapis.com/css2?family=Montserrat:wght@400;500;600;700&display=swap">
<style>
  :root {
    --page: #eceef1;
    --silver-light: #f7f8f9;
    --silver-mid: #d9dcdf;
    --silver-dark: #b9bdc2;
    --navy: #0d1620;
    --navy-soft: #1a2632;
    --gold: #c9a45c;
    --gold-light: #e9cf8e;
    --ink: #2a2f36;
    --white: #ffffff;
  }
  * { box-sizing: border-box; margin: 0; padding: 0; }
  html, body {
    width: 1200px;
    height: 1200px;
    overflow: hidden;
    background: var(--page);
    font-family: "Montserrat", sans-serif;
  }
  .canvas {
    position: relative;
    width: 1200px;
    height: 1200px;
    display: flex;
    align-items: center;
    justify-content: center;
  }
  .signature {
    position: relative;
    width: 1120px;
    height: 214px;
    border-radius: 6px;
    overflow: hidden;
    box-shadow: 0 10px 30px rgba(0, 0, 0, 0.12);
  }
  .signature__shapes {
    position: absolute;
    inset: 0;
    width: 100%;
    height: 100%;
  }
  .brand {
    position: absolute;
    left: 56px;
    top: 82px;
    display: flex;
    align-items: center;
    gap: 14px;
  }
  .brand__square {
    width: 20px;
    height: 20px;
    background: var(--gold);
  }
  .brand__name {
    font-size: 28px;
    font-weight: 600;
    letter-spacing: 1px;
    color: var(--ink);
    white-space: nowrap;
  }
  .person {
    position: absolute;
    right: 90px;
    top: 18px;
    text-align: center;
  }
  .person__name {
    font-size: 31px;
    font-weight: 700;
    color: var(--ink);
    line-height: 1.1;
  }
  .person__role {
    font-size: 17px;
    font-weight: 500;
    color: var(--gold);
    margin-top: 2px;
  }
  .contacts {
    position: absolute;
    top: 106px;
    display: flex;
    flex-direction: column;
    gap: 10px;
    list-style: none;
    color: var(--white);
    font-size: 13.5px;
    line-height: 1.35;
  }
  .contacts--left { left: 650px; }
  .contacts--right { left: 890px; }
  .contact {
    display: flex;
    align-items: flex-start;
    gap: 12px;
    white-space: nowrap;
  }
  .contact__icon {
    flex: none;
    width: 22px;
    height: 22px;
  }
</style>
</head>
<body>
<main class="canvas">
  <section class="signature" aria-label="Assinatura de e-mail Vendaluz Store">
    <svg class="signature__shapes" viewBox="0 0 1120 214" preserveAspectRatio="none" aria-hidden="true">
      <defs>
        <linearGradient id="silverBase" x1="0" y1="0" x2="1" y2="1">
          <stop offset="0" stop-color="#f7f8f9"/>
          <stop offset="0.45" stop-color="#d9dcdf"/>
          <stop offset="1" stop-color="#f7f8f9"/>
        </linearGradient>
        <linearGradient id="silverSheen" x1="0" y1="0" x2="1" y2="0">
          <stop offset="0" stop-color="#b9bdc2" stop-opacity="0.6"/>
          <stop offset="1" stop-color="#ffffff" stop-opacity="0"/>
        </linearGradient>
        <linearGradient id="goldStroke" x1="0" y1="0" x2="1" y2="0">
          <stop offset="0" stop-color="#c9a45c" stop-opacity="0"/>
          <stop offset="0.25" stop-color="#c9a45c"/>
          <stop offset="0.5" stop-color="#e9cf8e"/>
          <stop offset="1" stop-color="#c9a45c"/>
        </linearGradient>
        <linearGradient id="navyFill" x1="0" y1="0" x2="0" y2="1">
          <stop offset="0" stop-color="#1a2632"/>
          <stop offset="1" stop-color="#0d1620"/>
        </linearGradient>
      </defs>
      <rect class="base" width="1120" height="214" fill="url(#silverBase)"/>
      <path class="sheen" d="M0,0 L300,0 L120,214 L0,214 Z" fill="url(#silverSheen)"/>
      <path class="sheen" d="M380,0 L470,0 L340,214 L270,214 Z" fill="#ffffff" opacity="0.45"/>
      <path class="dark-band" d="M400,214 C480,205 500,110 580,92 C600,88 620,88 640,88 L1120,88 L1120,214 Z" fill="url(#navyFill)"/>
      <path class="gold-curve" d="M0,206 C200,212 430,196 490,130 C520,100 560,86 620,84 L1120,84" fill="none" stroke="url(#goldStroke)" stroke-width="4"/>
    </svg>

    <div class="brand">
      <span class="brand__square"></span>
      <span class="brand__name">Vendaluz Store</span>
    </div>

    <div class="person">
      <p class="person__name">Nome Sobrenome</p>
      <p class="person__role">Co- Founder</p>
    </div>

    <ul class="contacts contacts--left">
      <li class="contact">
        <svg class="contact__icon" viewBox="0 0 22 22" aria-hidden="true">
          <circle cx="11" cy="11" r="10" fill="none" stroke="#c9a45c" stroke-width="1.5"/>
          <path d="M7.5 6.5 L9.3 6.3 L10.2 8.6 L9.1 9.5 C9.7 10.9 11 12.2 12.4 12.8 L13.3 11.7 L15.6 12.6 L15.4 14.4 C11 14.6 7.3 10.9 7.5 6.5 Z" fill="#c9a45c"/>
        </svg>
        <span>+00 000-0000</span>
      </li>
      <li class="contact">
        <svg class="contact__icon" viewBox="0 0 22 22" aria-hidden="true">
          <circle cx="11" cy="11" r="10" fill="none" stroke="#c9a45c" stroke-width="1.5"/>
          <path d="M11 5.5 C8.7 5.5 7.2 7.2 7.2 9.2 C7.2 12 11 16.5 11 16.5 C11 16.5 14.8 12 14.8 9.2 C14.8 7.2 13.3 5.5 11 5.5 Z" fill="#c9a45c"/>
          <circle cx="11" cy="9.2" r="1.4" fill="#0d1620"/>
        </svg>
        <span>R. Seu Endereço - 00<br>Bairro - Cidade - Estado<br>CEP 0000-0000</span>
      </li>
    </ul>

    <ul class="contacts contacts--right">
      <li class="contact">
        <svg class="contact__icon" viewBox="0 0 22 22" aria-hidden="true">
          <circle cx="11" cy="11" r="10" fill="none" stroke="#c9a45c" stroke-width="1.5"/>
          <circle cx="11" cy="11" r="5.5" fill="none" stroke="#c9a45c" stroke-width="1.2"/>
          <ellipse cx="11" cy="11" rx="2.3" ry="5.5" fill="none" stroke="#c9a45c" stroke-width="1.2"/>
          <line x1="5.5" y1="11" x2="16.5" y2="11" stroke="#c9a45c" stroke-width="1.2"/>
        </svg>
        <span>www.vendaluz.com.br</span>
      </li>
      <li class="contact">
        <svg class="contact__icon" viewBox="0 0 22 22" aria-hidden="true">
          <circle cx="11" cy="11" r="10" fill="none" stroke="#c9a45c" stroke-width="1.5"/>
          <circle cx="11" cy="11" r="5.5" fill="none" stroke="#c9a45c" stroke-width="1.2"/>
          <ellipse cx="11" cy="11" rx="2.3" ry="5.5" fill="none" stroke="#c9a45c" stroke-width="1.2"/>
          <line x1="5.5" y1="11" x2="16.5" y2="11" stroke="#c9a45c" stroke-width="1.2"/>
        </svg>
        <span>www.vendaluz.com.br</span>
      </li>
    </ul>
  </section>
</main>
</body>
</html>
```